Poster Required for Cafe to promote Catering

I would like a Poster made to advertise that our business does catering.
On the poster we would like it to say:

Did you know that Lantern Pantry does Catering?
We offer Breakfast, Lunch, Morning and Afternoon Tea Options
Come instore to enquire

At the bottom of the flyer, can you please put the contact details:
Phone 0472 918 604
Email mia@lanternpantrykitchen.com

Poster Size A3

I have attached our logo and menu's so you can get a feel for what we like.

Target Market(s)

Hospital Staff: Doctors, Nurses, Admin

Industry/Entity Type

Hospitality

Requirements
Nice to have
• Some pictures of catering. Eg. Gourmet Sandwiches, Sliders
• You could check our instagram page for ideas on what we do..
• @lntpantry_qld

```html
<!DOCTYPE html>
<html lang="en">
<head>
<meta charset="utf-8">
<title>Lantern Pantry Catering Poster</title>
<link rel="stylesheet" href="https://fonts.googleapis.com/css2?family=Comfortaa:wght@400;700&display=swap">
<style>
  :root {
    --slate: #5b5b5b;
    --slate-dark: #4a4a4a;
    --band: #2a2a2a;
    --ink: #1f1b1b;
    --lemon: #f1e9a0;
    --olive: #c9c88a;
    --logo-panel: #c4c98e;
    --white: #f4f4f0;
  }
  * { margin: 0; padding: 0; box-sizing: border-box; }
  html, body { width: 867px; height: 1200px; overflow: hidden; background: var(--slate); }
  .poster {
    position: relative;
    width: 867px;
    height: 1200px;
    overflow: hidden;
    font-family: "Comfortaa", sans-serif;
    color: var(--white);
    background: radial-gradient(ellipse at 50% 45%, #676767 0%, var(--slate) 55%, var(--slate-dark) 100%);
  }
  .top-band {
    position: absolute; left: 0; top: 0; width: 100%; height: 58px;
    background: var(--band);
    border-bottom: 2px solid var(--olive);
  }
  .brand-panel {
    position: absolute; left: 273px; top: 117px; width: 337px; height: 292px;
    background: var(--logo-panel);
    display: flex; align-items: center; justify-content: center;
  }
  .brand-name {
    font-size: 38px; font-weight: 400; letter-spacing: 4px;
    color: var(--ink); text-align: center; line-height: 1.3;
    text-transform: uppercase;
  }
  .divider {
    position: absolute; left: 80px; width: 707px; height: 3px;
    background: var(--lemon);
  }
  .divider--upper { top: 481px; }
  .divider--lower { top: 876px; }
  .headline, .offer { position: absolute; white-space: nowrap; }
  .accent { color: var(--lemon); font-size: 46px; }
  .plain { font-size: 31px; }
  .gap { margin-left: 12px; }
  .headline--one { left: 56px; top: 535px; }
  .headline--two { left: 56px; top: 598px; }
  .offer .accent { font-size: 48px; }
  .offer .plain { font-size: 32px; }
  .offer--one { left: 197px; top: 671px; }
  .offer--two { left: 127px; top: 733px; }
  .ribbon { position: absolute; left: 22px; top: 955px; width: 823px; height: 110px; }
  .ribbon-text {
    position: absolute; left: 0; top: 972px; width: 867px;
    text-align: center; font-size: 55px; white-space: nowrap;
  }
  .ribbon-text .accent { font-size: 55px; }
  .contact-band {
    position: absolute; left: 0; top: 1106px; width: 100%; height: 94px;
    background: var(--band);
    border-top: 2px solid var(--olive);
    text-align: center; font-size: 26px; line-height: 38px; padding-top: 9px;
  }
  .contact-label { color: var(--lemon); }
</style>
</head>
<body>
<main class="poster">
  <div class="top-band"></div>

  <div class="brand-panel">
    <p class="brand-name">Lantern<br>Pantry</p>
  </div>

  <div class="divider divider--upper"></div>

  <p class="headline headline--one"><span class="accent">Did you know</span><span class="plain gap">the Lantern Pantry</span></p>
  <p class="headline headline--two"><span class="plain">does Catering?</span></p>

  <p class="offer offer--one"><span class="plain">We offer </span><span class="accent">Breakfast, Lunch</span><span class="plain"> and</span></p>
  <p class="offer offer--two"><span class="accent">Morning</span><span class="plain"> &amp; </span><span class="accent">Afternoon</span><span class="plain"> Tea Options</span></p>

  <div class="divider divider--lower"></div>

  <svg class="ribbon" viewBox="0 0 823 110" aria-hidden="true">
    <polygon points="0,4 823,4 790,55 823,106 0,106 33,55" fill="#c9c88a"/>
    <polygon points="8,10 815,10 783,55 815,100 8,100 40,55" fill="#242424"/>
  </svg>
  <p class="ribbon-text"><span class="accent">Come</span> instore to enquire</p>

  <footer class="contact-band">
    <p><span class="contact-label">Phone:</span> 0472 918 604</p>
    <p><span class="contact-label">Email:</span> mia@lanternpantrykitchen.com</p>
  </footer>
</main>
</body>
</html>
```